Business Card Design

We are a cutting edge natural health care provider who specializes in neuro behavioral conditions. We use brain mapping, neurofeedback, functional neurology and functional medicine to help people achieve their health goals.
We need a business card design for a new office. Would like to position ourselves as an upscale/concierge level treatment center that provides hope and results to people with chronic conditions. We would like the card to feature a brain, possibly a die cut shape. Design needs to communicate our tag line of "providing excellent care for difficult cases."
On back side of card:
By retraining abnormal brainwave patterns and eliminating metabolic problems, our programs often improve symptoms of:
ADD/ADHD
Addiction
Anxiety
Autism
Depression
Fibromyalgia
Insomnia
Memory Loss
Sensory/Motor Dysfunction

Target Market(s)

30-60 year olds with chronic conditions (Anxiety, depression,) or parents of children with chronic conditions (ADHD, autism, learning disorders, etc)

Industry/Entity Type

Health

Contact Information for Business Card

The Halvey Clinic
Dr. Colin Halvey, DC
2641 Orchard Pkwy. Suite 207
Duluth, GA 30097
(770) 555-0148
Fax (770) 555-0193
www.TheHalveyClinic.example
www.DrColinHalvey.example

Requirements
Nice to have
• Picture of a brain that really pops on the page.

```html
<!DOCTYPE html>
<html lang="en">
<head>
<meta charset="utf-8">
<title>The Halvey Clinic – Business Card</title>
<link rel="stylesheet" href="https://fonts.googleapis.com/css2?family=Source+Sans+3:wght@400;600;700&display=swap">
<style>
  :root {
    --canvas-bg: #e9e6e1;
    --card-white: #ffffff;
    --brand-yellow: #fff200;
    --ink: #1c1c1c;
    --mark-black: #222222;
  }
  * { margin: 0; padding: 0; box-sizing: border-box; }
  html, body {
    width: 1200px; height: 800px; overflow: hidden;
    background: var(--canvas-bg);
    font-family: "Source Sans 3", sans-serif;
    color: var(--ink);
  }
  .stage {
    width: 1200px; height: 800px;
    display: flex; align-items: center; justify-content: center;
  }
  .card {
    position: relative;
    width: 1050px; height: 600px;
    background: var(--card-white);
    box-shadow: 0 6px 24px rgba(0,0,0,0.18);
    overflow: hidden;
  }
  .card__swoosh {
    position: absolute; inset: 0;
    width: 100%; height: 100%;
  }
  .card__doctor {
    position: absolute;
    top: 52px; right: 120px;
    font-size: 44px; font-weight: 600;
    letter-spacing: 0.2px;
  }
  .brand {
    position: absolute;
    left: 120px; top: 120px;
    width: 330px;
  }
  .brand__dot {
    display: block;
    width: 230px; height: 230px;
    margin-left: 25px;
    border-radius: 50%;
    background: var(--mark-black);
  }
  .brand__name {
    margin-top: 95px;
    font-size: 44px; font-weight: 700;
    letter-spacing: -1px;
    white-space: nowrap;
  }
  .contact {
    position: absolute;
    left: 715px; top: 290px;
    font-size: 17px; line-height: 23px;
    font-weight: 400;
  }
  .contact__row { display: flex; }
  .contact__label { width: 52px; }
</style>
</head>
<body>
<main class="stage">
  <article class="card">
    <svg class="card__swoosh" viewBox="0 0 1050 600" preserveAspectRatio="none" aria-hidden="true">
      <path fill="var(--brand-yellow)"
            d="M955 0 C 915 230, 760 420, 420 470 C 250 495, 110 540, 0 600 L 1050 600 L 1050 0 Z"/>
    </svg>

    <h1 class="card__doctor">Dr. Colin Halvey</h1>

    <div class="brand">
      <span class="brand__dot" aria-hidden="true"></span>
      <p class="brand__name">The Halvey Clinic</p>
    </div>

    <address class="contact" style="font-style: normal;">
      <div class="contact__row"><span class="contact__label">Tel:</span><span>(770) 555-0148</span></div>
      <div class="contact__row"><span class="contact__label">Fax:</span><span>(770) 555-0193</span></div>
      <div>www.TheHalveyClinic.example</div>
      <div>www.DrColinHalvey.example</div>
      <div>DC 2641 Orchard Pkwy.</div>
      <div>Suite 207 Duluth, GA 30097</div>
    </address>
  </article>
</main>
</body>
</html>
```